Bref créative
Stationery - Business Card / Letterhead
For Public Adjusting Company
Professional
Doran T. Whitcombe
Sr. Public Adjuster
58 W. Alder St.
Suite 612
Harborview, NY 11492
doran@trclaimpro.com
www.trclaimpro.com
On the front I want our logo with the shadow on the bottom
On the back I would like you to incorporate a little creative usage of either the shield/lighthouse logo and all of my information
This logo should be used as the front as it has the bottom shadow which for some reason is not showing up on the other logos
the business card front will be high gloss finish
Also the fax number should be 516.843.9075 not 829. there is no where else for me to edit that once the project is uploaded

```html
<!DOCTYPE html>
<html lang="en">
<head>
<meta charset="utf-8">
<title>TR Claim Advisors – Stationery Set</title>
<link rel="stylesheet" href="https://fonts.googleapis.com/css2?family=Cinzel:wght@600&family=Open+Sans:wght@400;600&display=swap">
<style>
  :root {
    --navy: #0b3a78;
    --navy-deep: #072a5a;
    --blue: #1d5fae;
    --red: #d6232f;
    --red-deep: #b3141f;
    --paper: #ffffff;
    --ghost: #e6ecf4;
    --ink: #3a4a5e;
    --stage: #ffffff;
  }
  * { box-sizing: border-box; margin: 0; padding: 0; }
  html, body { width: 1200px; height: 737px; overflow: hidden; background: var(--stage); }
  body { position: relative; font-family: "Open Sans", Arial, sans-serif; color: var(--ink); }

  .sheet, .envelope, .card {
    position: absolute;
    background: var(--paper);
    box-shadow: 0 2px 6px rgba(0,0,0,.18);
    overflow: hidden;
  }

  /* Brand lockup */
  .lockup { display: flex; align-items: center; gap: 6px; background: var(--paper); padding: 5px 8px; }
  .lockup-square { width: 14px; height: 14px; background: var(--navy); flex: none; }
  .lockup-name { font-family: "Cinzel", Georgia, serif; font-weight: 600; color: var(--red); line-height: 1; white-space: nowrap; }
  .lockup--light { background: none; }
  .lockup--light .lockup-name { color: var(--paper); }
  .lockup--light .lockup-square { background: var(--paper); }

  /* Letterhead */
  .letterhead { left: 70px; top: 14px; width: 441px; height: 682px; }
  .letterhead-band {
    position: absolute; left: 0; top: 0; width: 100%; height: 50px;
    background: linear-gradient(180deg, var(--blue), var(--navy-deep));
    border-bottom: 3px solid var(--red);
  }
  .letterhead .lockup { position: absolute; left: 12px; top: 10px; height: 40px; }
  .letterhead .lockup-name { font-size: 19px; }
  .letterhead-mark {
    position: absolute; left: 60px; top: 230px; width: 180px; height: 420px;
    background: linear-gradient(180deg, var(--ghost), #eef2f8);
    border-radius: 80px 80px 4px 4px;
  }
  .letterhead-footer {
    position: absolute; left: 0; bottom: 10px; width: 100%;
    text-align: center; font-size: 7px; color: var(--ink);
  }

  /* Envelope */
  .envelope { left: 516px; top: 19px; width: 672px; height: 365px; }
  .envelope-flap { position: absolute; left: 0; top: 0; width: 100%; height: 230px; }
  .envelope-flap-url {
    position: absolute; left: 0; top: 22px; width: 100%; text-align: center;
    font-size: 6px; letter-spacing: .5px; color: rgba(255,255,255,.85);
  }
  .envelope-flap .lockup { position: absolute; left: 50%; top: 50px; transform: translateX(-50%); }
  .envelope-flap .lockup-name { font-size: 11px; }
  .envelope .lockup--return { position: absolute; left: 40px; top: 142px; height: 40px; }
  .lockup--return .lockup-name { font-size: 19px; }
  .envelope-window {
    position: absolute; left: 55px; top: 252px; width: 226px; height: 75px;
    border: 1px solid #c9d2de; border-radius: 6px; background: #f7f9fc;
  }
  .envelope-mark {
    position: absolute; left: 450px; top: 180px; width: 140px; height: 185px;
    background: linear-gradient(180deg, var(--ghost), #f1f4f9);
    border-radius: 60px 60px 0 0;
  }
  .envelope-address { position: absolute; left: 40px; bottom: 14px; font-size: 7px; }
  .envelope-rule { position: absolute; left: 0; bottom: 0; width: 100%; height: 5px; background: var(--red); }

  /* Business cards */
  .card { width: 204px; height: 96px; }
  .card-back { left: 720px; top: 473px; background: linear-gradient(180deg, var(--blue), var(--navy-deep)); }
  .card-white { left: 965px; top: 473px; }
  .card-blue { left: 720px; top: 595px; background: radial-gradient(ellipse at 50% 40%, var(--blue), var(--navy-deep)); }
  .card-red { left: 965px; top: 595px; background: radial-gradient(ellipse at 50% 40%, #e8424c, var(--red-deep)); }

  .card-back-mark {
    position: absolute; left: 14px; top: 8px; width: 56px; height: 88px;
    background: linear-gradient(180deg, rgba(255,255,255,.22), rgba(255,255,255,.06));
    border-radius: 24px 24px 0 0;
  }
  .card-back-details {
    position: absolute; left: 96px; top: 10px; color: var(--paper);
    font-size: 5px; line-height: 7px;
  }
  .card-back-name { font-size: 7px; font-weight: 600; line-height: 9px; }
  .card-back-title { margin-bottom: 4px; }
  .card-back-rule { position: absolute; left: 0; bottom: 0; width: 100%; height: 3px; background: var(--red); }

  .card .lockup { position: absolute; left: 50%; top: 34px; transform: translateX(-50%); padding: 3px 5px; }
  .card .lockup-name { font-size: 9px; }
  .card .lockup-square { width: 9px; height: 9px; }
  .card-url {
    position: absolute; left: 0; bottom: 12px; width: 100%; text-align: center;
    font-size: 5px; letter-spacing: .4px; color: rgba(255,255,255,.85);
  }
  .card-white .card-url { color: var(--ink); }
</style>
</head>
<body>

  <!-- Letterhead -->
  <section class="sheet letterhead" aria-label="Letterhead">
    <div class="letterhead-band"></div>
    <div class="lockup">
      <span class="lockup-square"></span>
      <span class="lockup-name">TR Claim Advisors</span>
    </div>
    <div class="letterhead-mark" role="img" aria-label="Faint lighthouse watermark"></div>
    <p class="letterhead-footer">58 W. Alder St., Suite 612, Harborview, NY 11492 | Toll Free 800.555.0142 | Fax 516.843.9075 | www.trclaimpro.com</p>
  </section>

  <!-- Envelope -->
  <section class="envelope" aria-label="Envelope">
    <div class="envelope-flap">
      <svg width="672" height="230" viewBox="0 0 672 230" preserveAspectRatio="none" aria-hidden="true">
        <defs>
          <linearGradient id="flapFill" x1="0" y1="0" x2="0" y2="1">
            <stop offset="0" stop-color="#1d5fae"/>
            <stop offset="1" stop-color="#072a5a"/>
          </linearGradient>
        </defs>
        <path d="M0 0 H672 V130 Q336 110 0 125 Z" fill="url(#flapFill)"/>
      </svg>
      <p class="envelope-flap-url">www.trclaimpro.com</p>
      <div class="lockup">
        <span class="lockup-square"></span>
        <span class="lockup-name">TR Claim Advisors</span>
      </div>
    </div>
    <div class="lockup lockup--return">
      <span class="lockup-square"></span>
      <span class="lockup-name">TR Claim Advisors</span>
    </div>
    <div class="envelope-mark" role="img" aria-label="Faint lighthouse watermark"></div>
    <div class="envelope-window"></div>
    <p class="envelope-address">58 W. Alder St., Suite 612, Harborview, NY 11492</p>
    <div class="envelope-rule"></div>
  </section>

  <!-- Business card back -->
  <section class="card card-back" aria-label="Business card back">
    <div class="card-back-mark" role="img" aria-label="Faint lighthouse graphic"></div>
    <div class="card-back-details">
      <p>58 W. Alder St., Suite 612</p>
      <p>Harborview, NY 11492</p>
      <p>Toll Free 800.555.0142</p>
      <p style="margin-bottom:4px">Fax 516.843.9075</p>
      <p class="card-back-name">Doran T. Whitcombe</p>
      <p class="card-back-title">Sr. Public Adjuster</p>
      <p>doran@trclaimpro.com</p>
      <p>www.trclaimpro.com</p>
    </div>
    <div class="card-back-rule"></div>
  </section>

  <!-- Business card front: white -->
  <section class="card card-white" aria-label="Business card front, white">
    <div class="lockup">
      <span class="lockup-square"></span>
      <span class="lockup-name">TR Claim Advisors</span>
    </div>
    <p class="card-url">www.trclaimpro.com</p>
  </section>

  <!-- Business card front: blue -->
  <section class="card card-blue" aria-label="Business card front, blue">
    <div class="lockup lockup--light">
      <span class="lockup-square"></span>
      <span class="lockup-name">TR Claim Advisors</span>
    </div>
    <p class="card-url">www.trclaimpro.com</p>
  </section>

  <!-- Business card front: red -->
  <section class="card card-red" aria-label="Business card front, red">
    <div class="lockup lockup--light">
      <span class="lockup-square"></span>
      <span class="lockup-name">TR Claim Advisors</span>
    </div>
    <p class="card-url">www.trclaimpro.com</p>
  </section>

</body>
</html>
```